Clockharbour Homepage Banner 1060 W x 100 H

Please see the attached 'word' document (Also copied below)
Feel free to use any images or logos from our website.
www.clockharbour.com.au

Background:
We are an Australian based official watch distributor/online retailer of international watch brands.

We require a new banner ad (1060 W x 100 H) to replace the existing one on our homepage www.clockharbour.com.au & wish to convey the following information:
*(Please feel free to alter wording, include or exclude points below & generally take creative license (with commercial reality in mind). We sell some luxury watches, so it must look professional & maintain a luxury look & feel.)

Clockharbour Direct:
Revolutionising the retail watch market !

- Buy direct from the official distributor & get world competitive
online prices (with full international warranty, & all original
papers, box & invoice)

- Eliminate all risk of fakes & non-existent factory warranty from
'grey' market sellers

- Free worldwide delivery over A$300

- Order online & 'try-on' in the comfort of your own home.
If you're not 100% happy, just post it back for a full refund or
exchange within 30 days

- Prefer to see & try on before purchase? Visit one of our retail
partner stores.

*** Feel free to copy any images from our website
www.clockharbour.com.au
Updates

Target Market(s)

Luxury watches

Industry/Entity Type

Retail

Font styles to use
Sans Serif

Requirements
Must have
• Visual imagery, text
Nice to have
• Feel free to use your creativity...
Should not have
• Cheap looking or tacky images. We sell some luxury watches, so we need to keep a professional & luxury image.

```html
<!DOCTYPE html>
<html lang="en">
<head>
<meta charset="utf-8">
<title>Clockharbour Homepage Banner</title>
<link href="https://fonts.googleapis.com/css2?family=Open+Sans:wght@300;400;600;700&display=swap" rel="stylesheet">
<style>
  :root {
    --navy: #0c2b66;
    --white: #ffffff;
    --ink: #111111;
    --gold: #b8955a;
    --muted: #444444;
    --steel-light: #dfe3e8;
    --steel-mid: #9aa3ad;
    --steel-dark: #2b2f35;
    --accent-blue: #1f8fd6;
  }
  * { margin: 0; padding: 0; box-sizing: border-box; }
  html, body { width: 1200px; height: 113px; overflow: hidden; background: var(--white); }
  .banner {
    position: relative;
    width: 1200px;
    height: 113px;
    font-family: "Open Sans", Arial, sans-serif;
    overflow: hidden;
  }
  .watch-imagery {
    position: absolute;
    left: 0; top: 0;
    width: 702px; height: 113px;
    background:
      radial-gradient(ellipse 90px 110px at 230px 95px, var(--accent-blue) 0%, var(--steel-dark) 55%, transparent 75%),
      radial-gradient(ellipse 130px 130px at 640px 40px, var(--white) 0%, var(--steel-light) 60%, var(--steel-mid) 85%, transparent 100%),
      linear-gradient(90deg, var(--steel-dark) 0%, var(--steel-mid) 30%, var(--steel-light) 60%, var(--white) 100%);
  }
  .delivery-offer {
    position: absolute;
    left: 0; top: 0;
    width: 668px; height: 74px;
    background: rgba(255,255,255,0.95);
    padding: 6px 0 0 12px;
  }
  .delivery-title {
    font-size: 35px;
    line-height: 40px;
    font-weight: 300;
    color: var(--ink);
    letter-spacing: 0.5px;
    white-space: nowrap;
  }
  .delivery-title .free { font-weight: 700; color: var(--gold); }
  .delivery-note {
    font-size: 11px;
    color: var(--muted);
    margin-top: 2px;
  }
  .why-us {
    position: absolute;
    left: 702px; top: 0;
    width: 498px; height: 113px;
    background: var(--navy);
    color: var(--white);
    padding: 11px 0 0 32px;
  }
  .why-us-title {
    font-size: 20px;
    font-weight: 400;
    letter-spacing: 0.5px;
    line-height: 26px;
  }
  .why-us-list {
    list-style: none;
    margin-top: 6px;
    font-size: 13.5px;
    line-height: 19px;
    font-weight: 400;
  }
  .why-us-list li::before { content: "- "; }
</style>
</head>
<body>
  <div class="banner">
    <div class="watch-imagery" role="img" aria-label="Close-up of luxury wristwatches with blue and steel dials"></div>
    <div class="delivery-offer">
      <h1 class="delivery-title"><span class="free">FREE</span> WORLDWIDE DELIVERY*</h1>
      <p class="delivery-note">*On All Orders Over $300AUD</p>
    </div>
    <div class="why-us">
      <h2 class="why-us-title">WHY CHOOSE US?</h2>
      <ul class="why-us-list">
        <li>World Competitive Online Pricing From The Official Distributor</li>
        <li>30 Day Refund Or Exchange Policy</li>
        <li>We Are Revolutionising the retail watch market</li>
      </ul>
    </div>
  </div>
</body>
</html>
```